Mosquito Repellent Wet Wipes pacakage design

We are a mosquito repellent manufacturer under the brand name "Zap Clear". We have a product currently and are looking to make it more attractive.

Our product is a mosquito repellent wipe that can be applied on skin and clothing for protection against mosquitoes. It is going to be available in sachets. Customer age groups include ages 10-30 as well as Moms who are key decision makers.

We are looking for a friendly package in terms of color and appeal and a redesign of Zap Clear logo. I am attaching our current product pictures and brochure. Hope this gets you started. We are attaching information on the spray bottle.

Visit www.velmorahealth.example for more details.

Package Dimension Folded : 80x60 mm
Package Dimension unfolded: 80 x 120 mm

Thank you
Ravi

Target Market(s)

General population with more focus on age groups 10-30 as well as Moms

Industry/Entity Type

Cosmetics

Requirements
Must have
• Statutory information should be provided on the product including Manufacturing address, ingredient name & bar code. I guess we can do this once the package is finalized

```html
<!DOCTYPE html>
<html lang="en">
<head>
<meta charset="utf-8">
<title>Zap Clear Mosquito Repellent Wipe – Sachet</title>
<link href="https://fonts.googleapis.com/css2?family=Yanone+Kaffeesatz:wght@300;400;600;700&display=swap" rel="stylesheet">
<style>
  :root{
    --paper:#ffffff;
    --leaf-dark:#2f4a1e;
    --leaf-mid:#4f7a2c;
    --leaf-light:#6a9a3a;
    --yellow:#f2f213;
    --yellow-soft:#e4e32a;
    --sky:#29abe2;
    --ink-light:#f2f2f2;
    --ink-muted:#d9dccf;
  }
  *{box-sizing:border-box;margin:0;padding:0}
  html,body{width:1200px;height:1200px;overflow:hidden;background:var(--paper)}
  body{position:relative;font-family:"Yanone Kaffeesatz",sans-serif;color:var(--ink-light)}

  .sachet{
    position:absolute;top:238px;width:554px;height:736px;overflow:hidden;
    background:radial-gradient(ellipse at 50% 55%,var(--leaf-light) 0%,var(--leaf-mid) 45%,var(--leaf-dark) 100%);
  }
  .sachet--front{left:33px}
  .sachet--back{left:616px}
  .sachet::before,.sachet::after{
    content:"";position:absolute;left:0;right:0;height:10px;z-index:3;
    background:
      linear-gradient(135deg,var(--paper) 50%,transparent 50%) 0 0/12px 10px repeat-x,
      linear-gradient(225deg,var(--paper) 50%,transparent 50%) 0 0/12px 10px repeat-x;
  }
  .sachet::before{top:0}
  .sachet::after{bottom:0;transform:scaleY(-1)}

  .leaf-backdrop{position:absolute;inset:0;
    background:radial-gradient(ellipse at 50% 50%,rgba(120,170,70,.25),rgba(20,40,10,.35));}

  .maker{position:absolute;display:flex;align-items:center;gap:10px}
  .maker__dot{width:32px;height:32px;border-radius:50%;background:var(--sky)}
  .maker__name{font-size:44px;font-weight:600;color:var(--yellow-soft);line-height:1}
  .sachet--front .maker{left:40px;top:52px}
  .sachet--back .maker{left:42px;top:138px}

  .count{position:absolute;right:36px;top:50px;text-align:right;line-height:1}
  .count__qty{font-size:28px;font-weight:700}
  .count__size{font-size:22px;font-weight:300}

  .product-mark{position:absolute;text-align:center;color:var(--yellow)}
  .product-mark__name{font-weight:700;line-height:.85;display:block}
  .product-mark__type{display:block;color:var(--ink-light);font-weight:600;letter-spacing:1px}
  .sachet--front .product-mark{left:112px;top:170px;width:355px}
  .sachet--front .product-mark__name{font-size:150px}
  .sachet--front .product-mark__type{font-size:24px;margin-top:14px}
  .sachet--back .product-mark{left:317px;top:72px;width:187px}
  .sachet--back .product-mark__name{font-size:78px}
  .sachet--back .product-mark__type{font-size:14px;margin-top:8px}

  .mascot{position:absolute;border-radius:50%;background:radial-gradient(circle,#5e8a30,#3c5b22)}
  .sachet--front .mascot{left:62px;top:440px;width:86px;height:62px;opacity:.8}

  .front-copy{position:absolute;left:0;right:0;top:560px;text-align:center}
  .front-copy__title{font-size:58px;font-weight:700;color:var(--yellow-soft);line-height:1}
  .front-copy__sub{font-size:36px;font-weight:400;color:var(--yellow-soft);line-height:1.05}
  .front-copy__claim{font-size:25px;font-weight:300;margin-top:14px;color:var(--ink-muted)}
  .front-copy__diseases{font-size:30px;font-weight:700;color:var(--ink-muted);margin-top:2px;line-height:1.1}

  .ingredients{position:absolute;left:50px;width:260px;top:214px;text-align:center;color:var(--yellow-soft)}
  .ingredients__title{font-size:40px;font-weight:700;line-height:1}
  .ingredients__list{font-size:24px;font-weight:400;margin-top:4px}

  .features{position:absolute;left:76px;top:326px;width:470px;list-style:none}
  .feature{display:flex;gap:30px;align-items:center;margin-bottom:18px}
  .feature__icon{flex:0 0 66px;width:66px;height:66px}
  .feature__title{font-size:26px;font-weight:700;line-height:1.05}
  .feature__text{font-size:20px;font-weight:400;line-height:1.15;color:var(--ink-muted)}
</style>
</head>
<body>

<section class="sachet sachet--front" aria-label="Sachet front">
  <div class="leaf-backdrop" role="img" aria-label="Soft background pattern of green leaves"></div>
  <div class="maker">
    <span class="maker__dot"></span>
    <span class="maker__name">Velmora</span>
  </div>
  <div class="count"><div class="count__qty">1 WIPE</div><div class="count__size">12x15 cm</div></div>
  <div class="mascot" role="img" aria-label="Cartoon mosquito mascot"></div>
  <div class="product-mark">
    <span class="product-mark__name">ZAP CLEAR</span>
    <span class="product-mark__type">ANTI - MOSQUITO</span>
  </div>
  <div class="front-copy">
    <h1 class="front-copy__title">Mosquito Repellent Wipe</h1>
    <p class="front-copy__sub">with olive extract</p>
    <p class="front-copy__claim">Long lasting protection from mosquitoes that may carry</p>
    <p class="front-copy__diseases">DENGUE, MALARIA &amp; CHIKUNGUNYA</p>
  </div>
</section>

<section class="sachet sachet--back" aria-label="Sachet back">
  <div class="leaf-backdrop" role="img" aria-label="Soft background pattern of green leaves"></div>
  <div class="product-mark">
    <span class="product-mark__name">ZAP CLEAR</span>
    <span class="product-mark__type">ANTI - MOSQUITO</span>
  </div>
  <div class="maker">
    <span class="maker__dot"></span>
    <span class="maker__name">Velmora</span>
  </div>
  <div class="ingredients">
    <h2 class="ingredients__title">Ingredients</h2>
    <p class="ingredients__list">DEET (15%), Others 85%</p>
  </div>
  <ul class="features">
    <li class="feature">
      <svg class="feature__icon" viewBox="0 0 66 66" aria-hidden="true">
        <circle cx="33" cy="33" r="30" fill="none" stroke="#f2f2f2" stroke-width="3"/>
        <circle cx="33" cy="33" r="23" fill="none" stroke="#f2f2f2" stroke-width="2"/>
        <path d="M33 16V33L44 44" fill="none" stroke="#f2f2f2" stroke-width="3" stroke-linecap="round"/>
      </svg>
      <div><h3 class="feature__title">8 Hours Protection</h3>
        <p class="feature__text">Zap Clear is applicable to all age groups.<br>It is applied on skin and clothing and provides<br>protection upto 8 hours.</p></div>
    </li>
    <li class="feature">
      <svg class="feature__icon" viewBox="0 0 66 66" aria-hidden="true">
        <path d="M60 6C30 6 8 20 8 44c0 8 4 14 8 16C20 36 34 24 48 20 34 28 24 40 20 60c28 0 40-26 40-54z" fill="#f2f2f2"/>
      </svg>
      <div><h3 class="feature__title">Skin friendly</h3>
        <p class="feature__text">Containing Olive Extracts, Vitamin E, Zap Clear is<br>uniquely formulated to have a pleasant experience</p></div>
    </li>
    <li class="feature">
      <svg class="feature__icon" viewBox="0 0 66 66" aria-hidden="true">
        <circle cx="33" cy="33" r="29" fill="none" stroke="#f2f2f2" stroke-width="4"/>
        <path d="M13 13L53 53" stroke="#f2f2f2" stroke-width="4"/>
      </svg>
      <div>
        <p class="feature__text">Zap Clear mosquito repellent sprays provide<br>protection from DENGUE, MALARIA &amp;<br>CHICKUNGUNYA Vectors by repelling them.<br>The active ingredient DEET works to mask the<br>odor emitted by human body and inhibits the<br>sensors of mosquitoes thereby repelling them</p></div>
    </li>
  </ul>
</section>

</body>
</html>
```